Business Card Design for videographer/filmmaker - Marek Dulin

Looking for a professional, creative, eye catching business card.
Target Market(s)
high end, big budget, businesses, producers, filmmakers, and studios
Industry/Entity Type
Business
Contact Information for Business Card
Please be creative and submit something original.
Font styles to use
Requirements
Must have
- Marek Dulin
- creative producer, writer, director, cinematographer, editor
- Pre-production, production, post-production

```html
<!DOCTYPE html>
<html lang="en">
<head>
<meta charset="utf-8">
<title>Marek Dulin – Business Card</title>
<link href="https://fonts.googleapis.com/css2?family=Roboto:wght@300;400&display=swap" rel="stylesheet">
<style>
  :root {
    --page: #ffffff;
    --card-front: #000000;
    --card-back: #121416;
    --ink-light: #e4e4e4;
    --ink-soft: #bdbdbd;
    --ink-mark: #b9b9b9;
    --accent-red: #8c2a26;
    --rule-grey: #8a8a8a;
  }
  * { margin: 0; padding: 0; box-sizing: border-box; }
  html, body {
    width: 1200px; height: 1000px; overflow: hidden;
    background: var(--page);
    font-family: "Roboto", Arial, sans-serif;
  }
  .canvas { position: relative; width: 1200px; height: 1000px; }

  .card { position: absolute; }
  .card--front {
    left: 78px; top: 82px; width: 647px; height: 389px;
    background: var(--card-front);
    display: flex; align-items: center; justify-content: center;
  }
  .brand-mark {
    display: flex; align-items: center; gap: 18px;
    color: var(--ink-mark);
    font-weight: 300; font-size: 58px; letter-spacing: 8px;
    margin-top: -18px;
  }
  .brand-mark__square {
    width: 14px; height: 14px; background: var(--ink-mark);
  }

  .card--back {
    left: 73px; top: 529px; width: 651px; height: 413px;
    background: var(--card-back);
  }
  .identity {
    position: absolute; left: 0; right: 0; top: 160px; text-align: center;
  }
  .identity__name {
    color: var(--ink-light);
    font-weight: 300; font-size: 50px; letter-spacing: 3px; line-height: 1;
  }
  .identity__roles {
    margin-top: 8px;
    color: var(--ink-light);
    font-size: 8.5px; letter-spacing: 1.1px; text-transform: uppercase;
  }
  .identity__roles .sep { color: var(--accent-red); margin: 0 3px; }
  .identity__phases {
    display: inline-block; margin-top: 8px; padding: 2px 6px;
    border-left: 1px solid var(--accent-red);
    border-right: 1px solid var(--accent-red);
    color: var(--ink-soft);
    font-size: 8px; letter-spacing: 0.3px; text-transform: uppercase;
  }
  .identity__phases strong { color: var(--ink-light); font-weight: 400; margin: 0 4px; }

  .contact-rule { position: absolute; left: 517px; top: 311px; }

  .contact {
    position: absolute; right: 27px; top: 328px;
    list-style: none; text-align: right;
    font-size: 15.5px; font-weight: 300; line-height: 20px;
  }
  .contact__label { color: var(--accent-red); }
  .contact__value { color: var(--ink-light); }
</style>
</head>
<body>
<main class="canvas">
  <section class="card card--front" aria-label="Card front">
    <div class="brand-mark">
      <span class="brand-mark__square"></span>
      <span class="brand-mark__name">DULIN</span>
    </div>
  </section>

  <section class="card card--back" aria-label="Card back">
    <div class="identity">
      <h1 class="identity__name">MAREK DULIN</h1>
      <p class="identity__roles">
        Creative producer<span class="sep">&gt;</span>Writer<span class="sep">&gt;</span>Director<span class="sep">&gt;</span>Cinematographer<span class="sep">&gt;</span>Editor
      </p>
      <p class="identity__phases">Pre-production <strong>Production</strong> Post-production</p>
    </div>

    <svg class="contact-rule" width="134" height="6" viewBox="0 0 134 6" aria-hidden="true">
      <defs>
        <linearGradient id="ruleFade" x1="0" x2="1" y1="0" y2="0">
          <stop offset="0" stop-color="#8a8a8a" stop-opacity="0"/>
          <stop offset="0.6" stop-color="#8a8a8a" stop-opacity="0.9"/>
          <stop offset="1" stop-color="#a0a0a0"/>
        </linearGradient>
      </defs>
      <rect x="0" y="0" width="134" height="6" fill="url(#ruleFade)"/>
    </svg>

    <ul class="contact">
      <li><span class="contact__label">website:</span> <span class="contact__value">marekdulin.com</span></li>
      <li><span class="contact__label">phone:</span> <span class="contact__value">1(408)555-0142</span></li>
      <li><span class="contact__label">email:</span> <span class="contact__value">film@marekdulin.com</span></li>
    </ul>
  </section>
</main>
</body>
</html>
```